Italian restaurant needs new site

Need to make our website better.

Must have reservation module

Must be able to sell wine tasting tours and wine pairing tours and intégrate with lumo desk

Blog

Social media

Wandermeter ranking and last review.

Number of Pages Required

1 page

Font styles to use
Serif

Requirements
Must have
• Reservation module
• Marketplace to buy wine pairings and gift certificates
• Wandermeter review
• Chatterbay posts
• All info from old site

```html
<!DOCTYPE html>
<html lang="en">
<head>
<meta charset="utf-8">
<title>Vinaria Bistro – Italian Cuisine & Wine Bar</title>
<link href="https://fonts.googleapis.com/css2?family=Open+Sans:wght@400;600&family=Pathway+Gothic+One&family=Kaushan+Script&display=swap" rel="stylesheet">
<style>
:root{
  --red:#e3000f;
  --wine:#9b1226;
  --wine-dark:#7d0e1d;
  --text:#333;
  --muted:#555;
  --cream:#fbe9c8;
  --grey-bg:#f2f2f2;
  --footer:#333;
  --green:#34a853;
}
*{box-sizing:border-box;margin:0;padding:0}
html,body{width:1200px;height:1200px;overflow:hidden;background:#fff}
body{position:relative;font-family:'Open Sans',sans-serif;color:var(--text)}
.abs{position:absolute}
.script{font-family:'Kaushan Script',cursive}
.cond{font-family:'Pathway Gothic One',sans-serif}
.btn{position:absolute;background:var(--wine);color:#fff;font-size:13px;display:flex;align-items:center;justify-content:center;text-transform:uppercase}

/* hero */
.hero{left:0;top:0;width:1200px;height:240px;background:linear-gradient(90deg,#cfd6c4 0%,#8ea55a 18%,#d8cfc6 33%,#5c4a48 50%,#6a4a3c 62%,#e6dccd 80%,#9a8a50 100%)}
.topbar{left:0;top:0;width:1200px;height:88px;background:rgba(247,232,228,.86)}
.brand{left:164px;top:34px;font-family:'Open Sans',sans-serif;font-weight:600;font-size:18px;color:var(--wine);white-space:nowrap}
.brand-mark{left:142px;top:38px;width:16px;height:16px;border-radius:50%;background:var(--wine)}
.contact{top:6px;font-size:12px;color:var(--red);display:flex;align-items:center;gap:4px}
.social{top:7px;width:11px;height:11px;background:#333;border-radius:50%}
.nav{top:44px;left:759px;display:flex;gap:31px;font-size:18px;color:var(--wine)}
.welcome{left:380px;top:121px;width:440px;height:67px;background:rgba(130,15,30,.82);border:1px solid #d7a0a0;display:flex;align-items:center;justify-content:center;color:var(--cream);font-size:30px;white-space:nowrap}
.dot{top:219px;width:9px;height:9px;border-radius:50%;background:#fff}

.section-title{left:0;width:1200px;text-align:center;color:var(--red);white-space:nowrap}
.divider{left:0;width:1200px;display:flex;justify-content:center;align-items:center;gap:8px}
.divider i{display:block;width:90px;border-top:1px solid #333;border-bottom:1px solid #333;height:3px}

.about-photo{left:132px;top:306px;width:170px;height:208px;background:linear-gradient(160deg,#5b3a2c,#c9a26b 45%,#b4453a 80%,#e8d8b8);border:2px solid #e6d3c0}
.about-text{left:318px;top:306px;width:424px;font-size:12.5px;line-height:16.8px;color:#333}
.about-text p{margin-bottom:12px}

.reserve{left:772px;top:306px;width:296px;height:208px;background:var(--red)}
.reserve h2{position:absolute;left:13px;top:6px;color:#fff;font-size:25px;font-weight:400}
.reserve .rule{position:absolute;left:13px;top:38px;width:54px;border-top:1px solid #fff}
.field{position:absolute;background:#f1f1f1;font-size:12px;color:#444;padding:7px 6px;height:26px}

/* services */
.band{left:0;top:530px;width:1200px;height:206px;background:linear-gradient(180deg,#fbe1c0 0%,#f7b04a 45%,#f39a0e 100%)}
.circle{top:541px;width:120px;height:120px;border-radius:50%;border:7px solid var(--cream)}
.svc-label{top:661px;width:240px;text-align:center;font-size:21px;color:#3a1a10}

/* menu */
.menu-bg{left:0;top:736px;width:1200px;height:286px;background:var(--grey-bg)}
.col-head{font-size:21px;color:var(--wine)}
.col-rule{width:54px;border-top:1px solid #333}
.thumb{width:97px;height:63px;border:1px solid #ddd}
.item-name{font-size:17px;color:#333;display:flex;align-items:baseline;gap:4px;white-space:nowrap}
.item-name .lead{flex:1;border-bottom:1px dotted #666;transform:translateY(-4px)}
.item-desc{font-size:11.5px;color:var(--muted);line-height:17px}

/* bottom */
.blog{left:132px;top:1035px;width:455px;height:133px;background:var(--red);color:#fff}
.widget{left:613px;top:1035px;width:216px;height:102px;background:linear-gradient(135deg,#3a0c12,#9a1a2a 40%,#c23a2e 70%,#4a0f18);border:2px solid #222}
.rating{left:853px;top:1035px;width:180px}
.footer{left:0;top:1174px;width:1200px;height:26px;background:var(--footer);color:#ddd;font-size:12px;display:flex;align-items:center;justify-content:center}
</style>
</head>
<body>

<!-- header -->
<div class="abs hero" role="img" aria-label="Photo banner: caesar salad, restaurant interior and grilled meat skewers"></div>
<div class="abs topbar"></div>
<div class="abs brand-mark"></div>
<div class="abs brand">Vinaria Bistro</div>

<div class="abs contact" style="left:760px">
  <svg width="10" height="10" viewBox="0 0 10 10"><path d="M2 0l2 2-1 1.5c.7 1.4 1.8 2.5 3.5 3.5L8 6l2 2-1.5 2C4 10 0 6 0 1.5z" fill="#e3000f"/></svg>+52 600 555 0142
</div>
<div class="abs" style="left:876px;top:4px;height:16px;border-left:1px solid #9b1226"></div>
<div class="abs contact" style="left:884px">
  <svg width="12" height="9" viewBox="0 0 12 9"><rect width="12" height="9" fill="#e3000f"/><path d="M0 0l6 5 6-5" stroke="#fff" fill="none"/></svg>+52 600 555
</div>
<div class="abs social" style="left:980px"></div>
<div class="abs social" style="left:1004px"></div>
<div class="abs social" style="left:1030px"></div>
<div class="abs social" style="left:1056px"></div>

<nav class="abs nav cond"><span>Home</span><span>About</span><span>Reservation</span><span>Blog</span><span>Contact</span></nav>

<div class="abs welcome script">Welcome to <span style="color:#f2c77a;margin-left:10px">Vinaria Bistro</span></div>
<div class="abs dot" style="left:583px;background:#c0392b"></div>
<div class="abs dot" style="left:596px"></div>
<div class="abs dot" style="left:608px"></div>

<!-- intro -->
<div class="abs section-title script" style="top:244px;font-size:30px">Vinaria Bistro italian restaurant in Cabo San Lucas</div>
<div class="abs divider" style="top:286px"><i></i><svg width="14" height="14" viewBox="0 0 14 14"><path d="M1 0h12L8 6v6h3v2H3v-2h3V6z" fill="#9b1226"/></svg><i></i></div>

<div class="abs about-photo" role="img" aria-label="Photo: antipasto board, bread basket and a bottle of white wine"></div>
<div class="abs about-text">
  <p>Vinaria Bistro Located in the heart of downtown, across from Plaza Marina Square, just two short blocks up from Harbor View Resort and the Cabo marina is Vinaria Bistro, a place with great original Southern Italian and Mediterranean cuisine and a European touch.</p>
  <p>We invite you to come and enjoy a glass of wine and to delight in our exquisite range of unique menu options. Created by hands with years of experience in traditional Mediterranean cuisine, our refreshing, family-style salads and tapas, Italian antipastos, fresh seafood dishes, and baked lasagna will transport your senses.</p>
</div>
<div class="btn" style="left:319px;top:482px;width:106px;height:32px">Read More</div>

<form class="abs reserve">
  <h2 class="script">Quick Reservation</h2>
  <div class="rule"></div>
  <div class="field" style="left:13px;top:56px;width:131px">Name</div>
  <div class="field" style="left:154px;top:56px;width:131px">Email</div>
  <div class="field" style="left:13px;top:88px;width:246px">Date &amp; Time</div>
  <svg style="position:absolute;left:266px;top:94px" width="14" height="14" viewBox="0 0 14 14"><rect x="0.5" y="2" width="13" height="11.5" fill="none" stroke="#fff"/><rect x="0.5" y="2" width="13" height="3" fill="#fff"/><g fill="#fff"><rect x="3" y="7" width="2" height="2"/><rect x="6" y="7" width="2" height="2"/><rect x="9" y="7" width="2" height="2"/><rect x="3" y="10" width="2" height="2"/><rect x="6" y="10" width="2" height="2"/></g></svg>
  <div class="field" style="left:13px;top:120px;width:131px">Table No.</div>
  <div class="field" style="left:154px;top:120px;width:131px">Phone</div>
  <div class="btn" style="left:109px;top:163px;width:80px;height:31px;background:var(--wine-dark)">Submit</div>
</form>

<!-- services -->
<div class="abs band" role="img" aria-label="Background photo: golden beer with bubbles"></div>
<div class="abs circle" style="left:220px;background:radial-gradient(circle at 50% 40%,#9be07a,#3a6a3a 60%,#2a2a2a)" role="img" aria-label="Photo: green cocktail in a martini glass"></div>
<div class="abs circle" style="left:540px;background:radial-gradient(circle at 50% 40%,#7a8a6a,#2a3028 60%,#1a1a1a)" role="img" aria-label="Photo: wine glass close-up"></div>
<div class="abs circle" style="left:860px;background:radial-gradient(circle at 50% 55%,#5a0a14,#3a2a2a 55%,#d8d0d0)" role="img" aria-label="Photo: glass of red wine"></div>
<div class="abs svc-label cond" style="left:160px">Wine tasting tours</div>
<div class="abs svc-label cond" style="left:480px">Wine pairing tours</div>
<div class="abs svc-label cond" style="left:800px">lumo desk</div>
<div class="btn" style="left:234px;top:691px;width:92px;height:32px">Read More</div>
<div class="btn" style="left:554px;top:691px;width:92px;height:32px">Read More</div>
<div class="btn" style="left:874px;top:691px;width:92px;height:32px">Read More</div>

<!-- menu -->
<div class="abs menu-bg"></div>
<div class="abs" style="left:1060px;top:740px;width:140px;height:120px;border-radius:40% 0 0 50%;background:radial-gradient(circle,#e08a4a,#f2e0cc 70%,transparent 72%)" role="img" aria-label="Photo: bowl of tomato soup with croutons"></div>
<div class="abs" style="left:0;top:880px;width:140px;height:142px;background:radial-gradient(circle at 40% 60%,#9ac25a,#dfe8c8 60%,transparent 72%)" role="img" aria-label="Photo: salad plate and wine glass"></div>

<div class="abs section-title script" style="top:744px;font-size:30px;color:var(--wine)">Best Menu</div>
<div class="abs divider" style="top:787px"><i></i><svg width="14" height="14" viewBox="0 0 14 14"><path d="M1 0h12L8 6v6h3v2H3v-2h3V6z" fill="#9b1226"/></svg><i></i></div>

<div class="abs col-head cond" style="left:132px;top:806px">Foods &amp; Aperitives</div>
<div class="abs col-rule" style="left:132px;top:838px;width:110px"></div>
<div class="abs thumb" style="left:133px;top:847px;background:linear-gradient(135deg,#e8e0d0,#a0562a 50%,#5a7a3a)" role="img" aria-label="Photo: spanish tortilla dish"></div>
<div class="abs item-name cond" style="left:240px;top:842px;width:348px"><span>Spanish tortilla</span><span class="lead"></span><span>$ 130</span></div>
<div class="abs item-desc" style="left:240px;top:869px">Traditional potato and egg tortilla</div>
<div class="abs thumb" style="left:133px;top:918px;background:linear-gradient(135deg,#eadcc0,#b84a2a 50%,#7a8a3a)" role="img" aria-label="Photo: bruschetta plate"></div>
<div class="abs item-name cond" style="left:240px;top:913px;width:348px"><span>Bruschetta Classica</span><span class="lead"></span><span>$ 120</span></div>
<div class="abs item-desc" style="left:240px;top:940px">Bread. Tomato. Garlic and basil</div>
<div class="btn" style="left:486px;top:992px;width:88px;height:26px;font-size:12px">View Foods</div>

<div class="abs col-head cond" style="left:612px;top:806px">Wines</div>
<div class="abs col-rule" style="left:612px;top:838px"></div>
<div class="abs thumb" style="left:613px;top:847px;background:linear-gradient(135deg,#3a2a1a,#e88a2a 50%,#7a4a2a)" role="img" aria-label="Photo: negroni cocktail"></div>
<div class="abs item-name cond" style="left:720px;top:842px;width:348px"><span>Negroni (Cocktail)</span><span class="lead"></span><span>$ 110</span></div>
<div class="abs item-desc" style="left:720px;top:869px">Lorem ipsum dolor sit amet ipsum.</div>
<div class="abs thumb" style="left:613px;top:918px;background:linear-gradient(135deg,#eadcc0,#b84a2a 50%,#7a8a3a)" role="img" aria-label="Photo: plated dish"></div>
<div class="abs item-name cond" style="left:720px;top:913px;width:348px"><span>Lambrusco, Casaletti ( Red )</span><span class="lead"></span><span>$ 300</span></div>
<div class="abs item-desc" style="left:720px;top:940px">By the Bottle<br>Lorem ipsum dolor sit amet, ipsum dolor sit amet. Ipsum sit amet.</div>
<div class="btn" style="left:972px;top:992px;width:87px;height:26px;font-size:12px">View Wines</div>

<!-- blog -->
<section class="abs blog">
  <div class="abs cond" style="left:9px;top:6px;font-size:22px">Our Blog</div>
  <div class="abs" style="left:9px;top:38px;width:54px;border-top:1px solid #fff"></div>
  <div class="abs" style="left:9px;top:44px;width:48px;height:36px;background:linear-gradient(135deg,#333,#a03040)" role="img" aria-label="Photo: restaurant sign"></div>
  <div class="abs cond" style="left:66px;top:45px;font-size:18px;font-style:italic">Lorem Ipsum Dolor</div>
  <div class="abs" style="left:66px;top:68px;font-size:11.5px">Dt: 7/8/2017</div>
  <div class="abs" style="left:241px;top:44px;width:48px;height:36px;background:linear-gradient(135deg,#f0f0e0,#9ac25a)" role="img" aria-label="Photo: salad"></div>
  <div class="abs cond" style="left:298px;top:45px;font-size:18px;font-style:italic">Lorem Ipsum Dolor</div>
  <div class="abs" style="left:298px;top:68px;font-size:11.5px">Dt: 7/8/2017</div>
  <div class="btn" style="left:137px;top:99px;width:78px;height:26px;font-size:11px;background:var(--wine-dark)">Read More</div>
  <div class="btn" style="left:369px;top:99px;width:78px;height:26px;font-size:11px;background:var(--wine-dark)">Read More</div>
</section>

<div class="abs widget" role="img" aria-label="Chatterbay page cover image">
  <div class="abs" style="left:8px;top:6px;width:50px;height:46px;background:#7a1a1a;border:2px solid #ddd"></div>
  <div class="abs" style="left:64px;top:6px;color:#fff;font-size:14px;font-weight:600;white-space:nowrap">Vinaria Bistro</div>
  <div class="abs" style="left:64px;top:25px;color:#fff;font-size:10.5px">3.469 likes</div>
  <div class="abs" style="left:8px;top:76px;background:#f4f4f4;color:#333;font-size:10.5px;padding:2px 6px;display:flex;gap:4px;align-items:center"><span style="width:9px;height:9px;background:#4a64a0;display:inline-block"></span>Chatterbay page</div>
</div>

<div class="abs rating">
  <div style="display:flex;align-items:center;gap:5px;font-size:19px;color:#222"><span style="width:14px;height:14px;border-radius:50%;background:#222;display:inline-block"></span>Wandermeter</div>
  <div style="font-size:11px;font-weight:600;text-decoration:underline;margin-top:2px">Vinaria Bistro</div>
  <div style="font-size:8px;font-weight:600;margin-top:6px">Traveler Rating</div>
  <div style="display:flex;gap:2px;margin-top:2px">
    <span style="width:8px;height:8px;border-radius:50%;background:var(--green)"></span><span style="width:8px;height:8px;border-radius:50%;background:var(--green)"></span><span style="width:8px;height:8px;border-radius:50%;background:var(--green)"></span><span style="width:8px;height:8px;border-radius:50%;background:var(--green)"></span><span style="width:8px;height:8px;border-radius:50%;background:var(--green)"></span>
  </div>
  <div style="font-size:7px;color:#999">Based on 1,090 traveler reviews</div>
  <div style="border-top:1px solid #ccc;margin-top:2px;width:174px"></div>
  <div style="font-size:9px;font-weight:600;margin-top:6px">Wandermeter Ranking</div>
  <div style="font-size:11px;color:var(--green);line-height:14px"><b>#9 of 575</b> places to eat in Cabo San Lucas</div>
</div>

<footer class="abs footer">copyright @Vinaria Bistro, 2017 &nbsp;|&nbsp; All Rights Reserved</footer>

</body>
</html>
```